Water ATM Card

Need a design for water ATM cards. Size of card is 3.375 x 2.125 inch
On the Front include the Cedar Brook Logo.
Bottom right corner should have Price $100
On the Back
This card is to be used to access water refills at any Cedar Brook Water Vending Machines.
Please contact (869) 415 2983 or (869) 238 4617 or email clearflowhub@mailbox-example.com for any assistance or recharging of card.

```html
<!DOCTYPE html>
<html lang="en">
<head>
<meta charset="utf-8">
<title>Cedar Brook Water ATM Card</title>
<link href="https://fonts.googleapis.com/css2?family=Montserrat:wght@400;600;700&display=swap" rel="stylesheet">
<style>
  :root {
    --canvas: #cbcbcb;
    --card-white: #ffffff;
    --brand-blue: #1769b3;
    --deep-blue: #27479b;
    --sky-blue: #2a8dd0;
    --leaf-green: #3fa83b;
    --text-white: #ffffff;
  }
  * { margin: 0; padding: 0; box-sizing: border-box; }
  html, body { width: 1200px; height: 1200px; overflow: hidden; }
  body { background: var(--canvas); font-family: 'Montserrat', sans-serif; position: relative; }

  .card {
    position: absolute;
    left: 308px;
    width: 584px;
    height: 367px;
    overflow: hidden;
    background: var(--card-white);
  }
  .card--front { top: 169px; }
  .card--back { top: 662px; }

  .brand {
    position: absolute;
    left: 0; right: 0;
    text-align: center;
    color: var(--brand-blue);
  }
  .brand__name {
    display: block;
    font-weight: 700;
    text-transform: uppercase;
    letter-spacing: 0.5px;
    line-height: 1;
  }
  .brand__tagline {
    display: block;
    font-weight: 400;
    line-height: 1.1;
  }
  .card--front .brand { top: 131px; }
  .card--front .brand__name { font-size: 31px; }
  .card--front .brand__tagline { font-size: 20px; }

  .front-sea {
    position: absolute;
    left: 0; right: 0;
    top: 262px;
    bottom: 0;
    background:
      linear-gradient(180deg, rgba(63,168,59,0.55) 0%, rgba(63,168,59,0) 22%),
      linear-gradient(90deg, var(--deep-blue) 0%, var(--sky-blue) 100%);
  }

  .price {
    position: absolute;
    right: 18px;
    bottom: 19px;
    color: var(--text-white);
    font-weight: 700;
    font-size: 24px;
  }

  .back-photo {
    position: absolute; inset: 0;
    background:
      radial-gradient(ellipse at 30% 0%, rgba(255,250,235,0.9), rgba(255,255,255,0) 55%),
      linear-gradient(170deg, #e9f1f3 0%, #c6dde3 35%, #d8e8ec 55%, #b9d4dc 75%, #dbe9ec 100%);
  }
  .card--back .brand { top: 140px; color: #1a5f9e; }
  .card--back .brand__name { font-size: 25px; }
  .card--back .brand__tagline { font-size: 17px; }

  .contact-band {
    position: absolute;
    left: 0; right: 0;
    top: 235px;
    height: 73px;
    background: linear-gradient(90deg, #1f4a96 0%, #2160a8 60%, #1f78bf 100%);
    color: var(--text-white);
    font-weight: 600;
    font-size: 19px;
    text-align: center;
    display: flex;
    flex-direction: column;
    justify-content: center;
    gap: 5px;
    line-height: 1.2;
  }
</style>
</head>
<body>

  <section class="card card--front">
    <div class="brand">
      <span class="brand__name">Cedar Brook</span>
      <span class="brand__tagline">Purified Spring Water</span>
    </div>
    <div class="front-sea" role="img" aria-label="Decorative green and blue wave artwork along the lower edge"></div>
    <div class="price">Price $100</div>
  </section>

  <section class="card card--back">
    <div class="back-photo" role="img" aria-label="Photograph of rolling ocean waves in soft blue light"></div>
    <div class="brand">
      <span class="brand__name">Cedar Brook</span>
      <span class="brand__tagline">Purified Spring Water</span>
    </div>
    <div class="contact-band">
      <p>Phone: (869) 415 2983 | (869) 238 4617</p>
      <p>Email: clearflowhub@mailbox-example.com</p>
    </div>
  </section>

</body>
</html>
```